Harriet Voss Consortium - Paediatric Lower Limb Surgery Agenda Forming Collective

A 2-sided A4 leaflet to explain the research priorities in Children's Orthopaedic Surgery.
We would like this to be similar to that produced previously by the physiotherapists.

```html
<!DOCTYPE html>
<html lang="en">
<head>
<meta charset="utf-8">
<title>Our Top-10 Research Priorities</title>
<link rel="stylesheet" href="https://fonts.googleapis.com/css2?family=EB+Garamond:wght@600&family=Roboto:ital,wght@0,400;0,700;1,400&display=swap">
<style>
  :root {
    --backdrop: #eef1f1;
    --paper: #f4f4f3;
    --ink: #2b2b2b;
    --teal: #13788a;
    --title-teal: #1d7f8f;
    --orange: #e0961e;
    --lime: #b7bf30;
    --slate: #8fb0b3;
    --white: #ffffff;
  }
  * { box-sizing: border-box; margin: 0; padding: 0; }
  html, body {
    width: 1200px; height: 1013px; overflow: hidden;
    background: var(--backdrop);
  }
  .leaflet {
    position: absolute;
    left: 266px; top: 20px;
    width: 637px; height: 928px;
    background: var(--paper);
    transform: scale(1.05);
    transform-origin: top left;
    box-shadow: 0 2px 10px rgba(0,0,0,0.08);
  }
  .title {
    position: absolute; left: 66px; top: 74px;
    font-family: "EB Garamond", serif; font-weight: 600;
    font-size: 27px; letter-spacing: 0.5px;
    color: var(--title-teal);
  }
  .priority-chain {
    position: absolute; left: 60px; top: 137px;
    width: 56px; height: 650px;
  }
  .priority-list {
    position: absolute; left: 125px; top: 137px;
    width: 450px; list-style: none;
  }
  .priority-list li {
    height: 65px; display: flex; align-items: center;
    font-family: "Roboto", sans-serif; font-size: 12.3px;
    line-height: 16.3px; color: var(--ink);
    text-align: justify; hyphens: auto;
  }
  .thanks-band {
    position: absolute; left: 0; top: 822px; width: 100%; height: 31px;
    background: var(--teal);
    font-family: "Roboto", sans-serif; font-style: italic;
    font-size: 11px; color: var(--white);
    padding-left: 43px; line-height: 31px;
  }
  .credits {
    position: absolute; left: 0; top: 853px; width: 100%; height: 75px;
    background: var(--orange);
  }
  .credits-heading {
    position: absolute; left: 43px; top: 20px;
    font-family: "Roboto", sans-serif; font-weight: 700;
    font-size: 26px; color: var(--white);
  }
  .credits-list {
    position: absolute; left: 332px; top: 16px; list-style: none;
    font-family: "Roboto", sans-serif; font-size: 8.6px;
    line-height: 11.2px; color: var(--white);
  }
</style>
</head>
<body>
  <article class="leaflet">
    <h1 class="title">OUR TOP-10 RESEARCH PRIORITIES</h1>

    <svg class="priority-chain" viewBox="0 0 56 650" aria-hidden="true">
      <rect x="21" y="32" width="14" height="586" fill="#e0961e"/>
      <g stroke="#e0961e" stroke-width="3.5">
        <circle cx="28" cy="32.5" r="19.5" fill="#e0961e"/>
        <circle cx="28" cy="97.5" r="19.5" fill="#b7bf30"/>
        <circle cx="28" cy="162.5" r="19.5" fill="#8fb0b3"/>
        <circle cx="28" cy="227.5" r="19.5" fill="#13788a"/>
        <circle cx="28" cy="292.5" r="19.5" fill="#b7bf30"/>
        <circle cx="28" cy="357.5" r="19.5" fill="#e0961e"/>
        <circle cx="28" cy="422.5" r="19.5" fill="#13788a"/>
        <circle cx="28" cy="487.5" r="19.5" fill="#8fb0b3"/>
        <circle cx="28" cy="552.5" r="19.5" fill="#b7bf30"/>
        <circle cx="28" cy="617.5" r="19.5" fill="#e0961e"/>
      </g>
      <g fill="#ffffff" font-family="Roboto, sans-serif" font-weight="700" font-size="24" text-anchor="middle">
        <text x="28" y="41">1</text>
        <text x="28" y="106">2</text>
        <text x="28" y="171">3</text>
        <text x="28" y="236">4</text>
        <text x="28" y="301">5</text>
        <text x="28" y="366">6</text>
        <text x="28" y="431">7</text>
        <text x="28" y="496">8</text>
        <text x="28" y="561">9</text>
        <text x="28" y="626" font-size="22">10</text>
      </g>
    </svg>

    <ol class="priority-list">
      <li>What are the best ways to measure the outcome following lower limb orthopaedic surgery in children?</li>
      <li>Following orthopaedic surgery to the lower limbs, what should children’s rehabilitation include, how long is it expected to last and how does it affect the result of treatment?</li>
      <li>What is the short-term and long-term clinical and cost effectiveness of orthopaedic lower limb surgery (including best timing and technique) for children with Cerebral Palsy who can walk?</li>
      <li>What are the short term and long term outcomes of surgery compared to non-surgical care in the treatment of Perthes disease of the hip?</li>
      <li>What is the clinical and cost effectiveness of pre-operative rehabilitation in children presenting with lower limb orthopaedic conditions?</li>
      <li>What is the short-term and long-term clinical and cost effectiveness of Selective Dorsal Rhizotomy (SDR) in children with Cerebral Palsy who can walk?</li>
      <li>Can surveillance and non-surgical treatment (e.g. physiotherapy, botulinum toxin injections, functional electrical stimulation, orthotics, casting) prevent the development of deformity requiring surgery in children with Cerebral Palsy?</li>
      <li>What is the best method of screening for Developmental Dysplasia of the Hip (DDH) in terms of clinical and cost effectiveness?</li>
      <li>What are the best strategies to optimise communication of information between patients/carers and clinicians in order to enable shared decision-making?</li>
      <li>What is the best management for hip displacement in children with Cerebral Palsy?</li>
    </ol>

    <p class="thanks-band">Many thanks to all those people who helped us take this work off the ground and helped us finish it!</p>

    <footer class="credits">
      <h2 class="credits-heading">Special thanks to:</h2>
      <ul class="credits-list">
        <li>The Northvale Society of Young Limb Surgery</li>
        <li>The Kestrel Bone &amp; Joint Association</li>
        <li>The University of Ashbrook and the</li>
        <li>Harriet Voss Consortium, who always look for fair play in research!</li>
      </ul>
    </footer>
  </article>
</body>
</html>
```